I need a business card design for my new chiropractic business.It is chiropractic that addresses the whole body, is natural, done by hand, will reduce pain, increase vitality, reduce stress. It is safe and suitable for all ages.I am a Ravenhale chiropractor and they have a particular logo see RCA.co.uk. I would like Spineleaf Chiropractic and Ravenhale to feature if possible. Purple colours and tones please.

Target Market(s)

People who are interested in their health and being empowered to take responsibility for their well being.

Industry/Entity Type

Business

Contact Information for Business Card

My name, Marla Denton
PSB Reg No 05192
Tel No 07914 118275

Font styles to use
Sans Serif
Other font styles liked:
• ITALIC?

Colors
b768aa
886aae
a6459a
6c459b
ffffff
e567a6

Requirements
Must have
• graphic to represent healing by hand and increase in well being. by restoring spinal and nervous system function.
• Professional and clear layout and information
• Some or all of the words above in project description
• Ravenhale logo (from ravenhalechiropractic.org).
Nice to have
• Transformative theme- body- from pain to freedom of motion. A more fully integrated
• System, better functioning and connections.
• Clear layout and message
Should not have
• Must not look tacky

```html
<!DOCTYPE html>
<html lang="en">
<head>
<meta charset="utf-8">
<title>Ravenhale Chiropractic – Business Card</title>
<link rel="stylesheet" href="https://fonts.googleapis.com/css2?family=Cinzel:wght@400;700&display=swap">
<style>
  :root {
    --page-bg: #ebebed;
    --card-white: #fbfbfb;
    --crimson: #c23a52;
    --plum: #5b2c6f;
    --deep-violet: #3b2562;
    --name-red: #9a2440;
    --ink: #4a4a4a;
    --brand-grey: #5d5d66;
    --swoosh-grey: #4f4f55;
    --white: #ffffff;
  }
  * { margin: 0; padding: 0; box-sizing: border-box; }
  html, body { width: 1200px; height: 2286px; overflow: hidden; }
  body {
    background: var(--page-bg);
    font-family: "Cinzel", serif;
    position: relative;
  }
  .card {
    position: absolute;
    left: 150px;
    width: 900px;
    height: 512px;
    overflow: hidden;
    box-shadow: 0 10px 26px rgba(0,0,0,0.22);
  }
  .card-front { top: 551px; background: var(--card-white); }
  .card-back {
    top: 1223px;
    background: linear-gradient(110deg, var(--crimson) 0%, #9a3a6a 45%, var(--deep-violet) 100%);
  }

  .brand {
    position: absolute;
    display: flex;
    align-items: center;
    gap: 18px;
    font-weight: 400;
    letter-spacing: 2px;
    white-space: nowrap;
  }
  .brand-mark { border-radius: 50%; flex: none; }
  .card-front .brand { left: 34px; top: 48px; color: var(--brand-grey); font-size: 40px; }
  .card-front .brand-mark { width: 76px; height: 76px; background: linear-gradient(120deg, var(--crimson), var(--plum)); }
  .card-back .brand { left: 0; right: 0; top: 188px; justify-content: center; color: var(--white); font-size: 48px; }
  .card-back .brand-mark { width: 96px; height: 96px; background: var(--white); }

  .card-waves { position: absolute; left: 0; top: 0; width: 900px; height: 512px; }

  .holder { position: absolute; left: 34px; top: 252px; }
  .holder-name { font-size: 27px; font-weight: 700; color: var(--name-red); letter-spacing: 0.5px; line-height: 1.2; }
  .holder-role { font-size: 18px; color: var(--ink); margin-top: 2px; line-height: 1.2; }

  .contacts { position: absolute; left: 34px; top: 334px; list-style: none; }
  .contacts li {
    display: flex; align-items: center; gap: 12px;
    font-size: 16px; color: var(--ink); height: 26px;
  }
  .contacts svg { width: 17px; height: 17px; fill: var(--name-red); flex: none; }

  .registration {
    position: absolute; left: 0; right: 0; bottom: 36px;
    text-align: center; color: var(--white); font-size: 24px; letter-spacing: 1px;
  }
</style>
</head>
<body>

<section class="card card-front" aria-label="Business card front">
  <svg class="card-waves" viewBox="0 0 900 512" aria-hidden="true">
    <defs>
      <linearGradient id="band-gradient" x1="0" y1="0" x2="1" y2="0">
        <stop offset="0" stop-color="#c23a52"/>
        <stop offset="0.5" stop-color="#8a3470"/>
        <stop offset="1" stop-color="#4e2a6c"/>
      </linearGradient>
    </defs>
    <path d="M0 440 C160 426 320 444 470 462 C640 482 780 462 900 404 L900 420 C780 480 640 498 470 478 C320 460 160 444 0 456 Z" fill="var(--swoosh-grey)"/>
    <path d="M0 476 C200 456 360 470 520 486 C660 498 790 480 900 436 L900 512 L0 512 Z" fill="url(#band-gradient)"/>
    <path d="M0 486 C200 468 360 482 520 498 C660 510 790 492 900 450 L900 456 C790 500 660 516 520 504 C360 490 200 476 0 494 Z" fill="var(--white)" opacity="0.85"/>
  </svg>

  <div class="brand"><span class="brand-mark"></span><span class="brand-name">Ravenhale Chiropractic</span></div>

  <div class="holder">
    <p class="holder-name">Marla Denton</p>
    <p class="holder-role">Founder &amp; CEO</p>
  </div>

  <ul class="contacts">
    <li>
      <svg viewBox="0 0 24 24"><path d="M3 9c0-3 4-5 9-5s9 2 9 5v2h-5V8.5C15 7.6 13.6 7 12 7s-3 .6-4 1.5V11H3z M6 12h12l2 8H4z"/></svg>
      <span>07914 118275</span>
    </li>
    <li>
      <svg viewBox="0 0 24 24"><path d="M2 5h20v14H2z M4 7v.4l8 5.4 8-5.4V7z" fill-rule="evenodd"/></svg>
      <span>admin@ravenhalechiropractic.org</span>
    </li>
    <li>
      <svg viewBox="0 0 24 24"><path d="M2 3h20v14H2z M4 5v10h16V5z M9 18h6v2h3v2H6v-2h3z" fill-rule="evenodd"/></svg>
      <span>www.ravenhalechiropractic.org</span>
    </li>
  </ul>
</section>

<section class="card card-back" aria-label="Business card back">
  <div class="brand"><span class="brand-mark"></span><span class="brand-name">Ravenhale Chiropractic</span></div>
  <p class="registration">PSB Reg No 05192</p>
</section>

</body>
</html>
```